依頼概要
・依頼の目的/概要
人生100年時代に、認知症や介護予防・改善に役立つ、化粧療法レクレーションの表紙デザインをお願いします。

・本の内容
高齢者の皆さんを抱えた、娘さん世代、ソーシャルビジネスとして取り組みたい女性、人の役に立ちたい・介護や医療関係者のスキルアップとして、心を癒すスキンタッチケアとしての化粧療法レクレーションを知って頂き、その効果を実例等で理解する事で、実践してみたくなる内容にしています。またお仕事としても、ボランティアとしても活躍できるセラピストの役割や募集にもふれています。
化粧療法レクレーションがどんなものか?!やるとどんな効果がきたいできるのか?!に、研究データーと実際の実例を交えて説明・解説した本です。

・デザイン要望
美容で心が癒される事が、伝わるようなイメージと解説でもあるので、化粧療法レクレーションのバイブルみたいな感じでしょうか?!(イメージカラーは、ピンクです。http://tkvb.or.jp tkvb-sora.com 色の感じです、参考資料)
もちろん、デザイナーさんのセンスにお任せします。

その他何かご不明な点がございましたら、お気軽にご質問ください。
よろしくお願いいたします。
■ 選んだ理由

認知症や介護の予防・改善を目指した療法ですので、見た方が、明るく安心し、そして楽しみになるイメージが持てるデザインを選びました。特に当選したものは、高齢者と若者が一緒に映る写真の印象が、表題のレクレーションのイメージに繋がるということが、一番の選定理由です。

■ 提案者全員のお礼・コメント

素晴らしい表紙のデザインの応募をいただき、本当に感謝しています。
選定は、本当に悩みました。いくつも表紙にしたい作品がありました。出して頂いた作品が、教科書的と、読み物的な提案を頂いたように思います。皆さん素晴らしかったのですが、今回は親しみやすさを重視させて頂きました。特に最初に応募して頂いた、pelmiさんの表紙には、私の言いたい事が網羅されていて、良かったです。が、今回のテーマを考えて、残念ながら選定致しませんでした。
次の機会に皆様とお仕事ができれば、嬉しいです。ありがとうございました。

```html
<!DOCTYPE html>
<html lang="ja">
<head>
<meta charset="utf-8">
<title>化粧療法レクレーション 表紙</title>
<link rel="stylesheet" href="https://fonts.googleapis.com/css2?family=M+PLUS+Rounded+1c:wght@500;700;800&display=swap">
<style>
  :root {
    --paper: #ffffff;
    --title-pink: #e9427c;
    --band-pink: #ef9fb5;
    --rule-pink: #ec6f96;
    --sub-ink: #6d5a5c;
    --author-pink: #e0407a;
    --figure-light: #f6d6cf;
    --figure-deep: #c9b9c6;
  }
  * { margin: 0; padding: 0; box-sizing: border-box; }
  html, body { width: 753px; height: 1200px; overflow: hidden; background: var(--paper); }
  .cover {
    position: relative; width: 753px; height: 1200px; overflow: hidden;
    background: var(--paper);
    font-family: "M PLUS Rounded 1c", sans-serif;
  }
  .top-rule { position: absolute; left: 0; top: 0; }
  .subtitle {
    position: absolute; top: 160px; left: 0; width: 100%;
    text-align: center; font-size: 36px; font-weight: 500; line-height: 1;
    color: var(--sub-ink); letter-spacing: 2px;
  }
  .title {
    position: absolute; left: 0; width: 100%; text-align: center;
    color: var(--title-pink); font-weight: 800; line-height: 1;
  }
  .title-main { top: 230px; font-size: 112px; letter-spacing: 2px; }
  .title-sub { top: 422px; font-size: 80px; letter-spacing: 0; }
  .divider { position: absolute; left: 0; top: 588px; }
  .band {
    position: absolute; left: 0; top: 658px; width: 753px; height: 440px;
    background: var(--band-pink);
  }
  .tagline {
    position: absolute; top: 676px; left: 186px;
    display: flex; flex-direction: row-reverse; gap: 58px;
    color: var(--paper); font-weight: 700;
  }
  .tagline-col { display: flex; flex-direction: column; width: 46px; }
  .tagline-col span {
    display: block; width: 46px; height: 45px;
    font-size: 42px; line-height: 45px; text-align: center;
  }
  .figure-art {
    position: absolute; left: 452px; top: 500px; width: 301px; height: 598px;
    border-radius: 150px 150px 0 0;
    background: linear-gradient(180deg, var(--figure-deep) 0%, var(--figure-light) 55%, #fbe9e5 100%);
  }
  .author {
    position: absolute; top: 1125px; left: 400px; line-height: 1;
    font-size: 54px; font-weight: 700; color: var(--author-pink);
    letter-spacing: 4px; white-space: nowrap;
  }
</style>
</head>
<body>
<div class="cover">
  <svg class="top-rule" width="753" height="80" viewBox="0 0 753 80" aria-hidden="true">
    <line x1="40" y1="38" x2="713" y2="38" stroke="var(--rule-pink)" stroke-width="3"/>
    <circle cx="376.5" cy="38" r="9" fill="var(--rule-pink)"/>
  </svg>

  <p class="subtitle">心を癒し、健康寿命を延ばす</p>
  <h1 class="title title-main">化粧療法</h1>
  <p class="title title-sub">レクレーション</p>

  <svg class="divider" width="753" height="30" viewBox="0 0 753 30" aria-hidden="true">
    <line x1="60" y1="15" x2="693" y2="15" stroke="var(--rule-pink)" stroke-width="2" stroke-dasharray="6 8"/>
    <circle cx="376.5" cy="15" r="7" fill="var(--rule-pink)"/>
  </svg>

  <div class="band"></div>
  <div class="tagline" aria-label="人生100年時代に認知症や介護予防・改善に役立つ">
    <p class="tagline-col"><span>人</span><span>生</span><span>１</span><span>０</span><span>０</span><span>年</span><span>時</span><span>代</span><span>に</span></p>
    <p class="tagline-col"><span>認</span><span>知</span><span>症</span><span>や</span><span>介</span><span>護</span><span>予</span><span>防</span><span>・</span></p>
    <p class="tagline-col"><span>改</span><span>善</span><span>に</span><span>役</span><span>立</span><span>つ</span></p>
  </div>
  <div class="figure-art" role="img" aria-label="手鏡を持って頬に触れる白髪の高齢女性のイラスト"></div>

  <p class="author">森　由紀子</p>
</div>
</body>
</html>
```